Creative Web Site to Sell Geology Classes for Homeschooling

I am starting a business to sell a variety of geology classes for homeschoolers. I am targeting classes for kids with dyslexia, although others will benefit as well. The classes will be delivered by mail. Each class will have a video, a manual, and rock samples. I need a landing page that I can link over to seven other pages, a page with a template for products, and a template of the pages that will not have products. All should be easy to edit. All pages should display well with handheld devices (phones), as well as desktops.

Designs look the same

```html
<!DOCTYPE html>
<html lang="en">
<head>
<meta charset="utf-8">
<title>Stonepath Academy – Geology Classes</title>
<link href="https://fonts.googleapis.com/css2?family=Montserrat:wght@600;700;800&family=Open+Sans:wght@400;600;700&display=swap" rel="stylesheet">
<style>
:root{
  --stage:#7d7d7d;
  --coral:#ee6b55;
  --teal:#5ccfa2;
  --purple:#5c4e79;
  --yellow:#f5b437;
  --green:#4fc08d;
  --paper:#ffffff;
  --mist:#f4f1f3;
  --ink:#333333;
  --muted:#777777;
  --night:#1f1f1f;
  --night-line:#3a3a3a;
}
*{box-sizing:border-box;margin:0;padding:0}
html,body{width:1200px;height:4945px;overflow:hidden}
body{background:var(--stage);font-family:"Open Sans",Arial,sans-serif;color:var(--ink);position:relative}
h1,h2,h3,h4,.brand,.btn,.nav a{font-family:"Montserrat",Arial,sans-serif}
.photo{position:absolute}

/* ===== desktop ===== */
.desk{position:absolute;left:36px;top:33px;width:894px}
.desk section,.desk header,.desk footer{position:relative;width:100%;overflow:hidden}
.d-header{height:89px;background:var(--paper)}
.brand{display:flex;align-items:center;gap:8px;font-weight:800;color:var(--coral);text-transform:uppercase;line-height:1}
.brand .mark{background:var(--coral);border-radius:50%;flex:none}
.d-header .brand{position:absolute;left:24px;top:18px;font-size:17px}
.d-header .brand .mark{width:40px;height:40px}
.follow{position:absolute;left:470px;top:22px;display:flex;align-items:center;gap:5px;font-size:8px;font-weight:600;color:var(--muted)}
.follow i{display:block;width:16px;height:16px;border-radius:50%;background:#1f8fd6}
.follow i:nth-child(3){background:#2a9fe0}
.follow i:nth-child(4){background:#0f6eab}
.call{position:absolute;left:630px;top:14px;display:flex;gap:8px;align-items:center}
.call .icon{width:24px;height:24px;background:#ddd;border-radius:3px;display:flex;align-items:center;justify-content:center}
.call small{display:block;font-size:8px;color:var(--muted);font-weight:600}
.call strong{display:block;font-family:"Montserrat",sans-serif;font-size:17px;color:var(--coral);font-weight:800;letter-spacing:.5px}
.nav{position:absolute;display:flex}
.nav a{color:#fff;text-decoration:none;text-transform:uppercase;font-weight:700;text-align:center;white-space:nowrap}
.nav a:nth-child(1){background:var(--coral)}
.nav a:nth-child(2){background:var(--teal)}
.nav a:nth-child(3){background:var(--yellow)}
.nav a:nth-child(4){background:var(--green)}
.nav a:nth-child(5){background:var(--purple)}
.d-header .nav{left:402px;top:64px}
.d-header .nav a{width:77px;height:25px;line-height:25px;font-size:9px}

.d-hero{height:415px;background:linear-gradient(120deg,#7b3d31 0%,#b45c49 35%,#d79b82 60%,#8d4a3b 100%)}
.d-hero h1{position:absolute;left:100px;top:88px;color:#fff;font-size:40px;line-height:44px;font-weight:800;text-transform:uppercase}
.btn{display:inline-block;background:var(--teal);color:#fff;font-weight:700;text-transform:uppercase;border-radius:3px;text-align:center}
.d-hero .btn{position:absolute;left:100px;top:210px;font-size:11px;padding:8px 18px}
.dots{position:absolute;display:flex;gap:6px}
.dots i{width:8px;height:8px;border-radius:50%;border:1px solid #fff}
.dots i.on{background:#fff}
.d-hero .dots{left:320px;bottom:20px}

.sec-title{text-align:center;font-weight:800;text-transform:uppercase;color:var(--ink)}
.sec-title::after{content:"";display:block;margin:8px auto 0;width:40px;height:3px;background:linear-gradient(90deg,var(--coral) 33%,var(--teal) 33% 66%,var(--yellow) 66%)}
.d-classes{height:492px;background:var(--mist)}
.d-classes .sec-title{position:absolute;top:44px;width:100%;font-size:21px}
.class-card{position:absolute;top:132px;width:171px;height:287px;box-shadow:0 3px 8px rgba(0,0,0,.18)}
.class-card .photo{position:relative;height:161px;width:100%}
.class-card .body{height:126px;padding:14px 12px;color:#fff}
.class-card h3{font-size:9px;font-weight:800;text-transform:uppercase;margin-bottom:6px}
.class-card p{font-size:8px;line-height:11px;margin-bottom:8px}
.class-card .btn{background:#fff;color:var(--ink);font-size:7px;padding:4px 8px}
.bg-coral{background:var(--coral)}.bg-teal{background:var(--teal)}.bg-purple{background:var(--purple)}

.d-welcome{height:399px;background:var(--paper)}
.welcome-text{position:absolute;left:106px;top:66px;width:300px}
.welcome-text h2{font-size:27px;line-height:30px;font-weight:800;color:var(--coral);text-transform:uppercase}
.welcome-text h2 span{color:var(--yellow);display:block}
.welcome-text h2::after{content:"";display:block;width:40px;height:3px;background:var(--yellow);margin:8px 0 10px}
.welcome-text p{font-size:9px;line-height:13px;color:var(--muted);margin-bottom:14px}
.welcome-text .btn{font-size:10px;padding:7px 14px}
.d-welcome .photo{left:442px;top:43px;width:346px;height:313px;background:linear-gradient(135deg,#d8dde4,#8a9bb0 55%,#4a5a70)}

.d-news{height:491px;background:var(--mist)}
.d-news .sec-title{position:absolute;top:40px;width:100%;font-size:21px}
.news-card{position:absolute;top:122px;width:214px;height:303px;background:#fff;box-shadow:0 2px 6px rgba(0,0,0,.12)}
.news-card .photo{position:relative;width:100%;height:138px;background:linear-gradient(135deg,#c9c2b6,#8b8578 60%,#5b564e)}
.news-card .body{padding:14px 16px}
.news-card h3{font-size:9px;line-height:12px;font-weight:800;text-transform:uppercase;margin-bottom:7px}
.news-card p{font-size:8px;line-height:11px;color:var(--muted);margin-bottom:9px}
.news-card .btn{font-size:7px;padding:4px 9px}

.d-testi{height:438px;background:var(--paper)}
.d-testi .sec-title{position:absolute;top:42px;width:100%;font-size:21px}
.quote{position:absolute;left:230px;top:120px;width:434px;text-align:center;font-size:12px;line-height:17px;color:var(--ink)}
.qmark{position:absolute;font-family:Georgia,serif;font-size:44px;color:var(--teal);font-weight:700;line-height:1}
.people{position:absolute;left:0;width:100%;top:270px;display:flex;justify-content:center;align-items:flex-start;gap:34px}
.person{text-align:center;font-size:7px;color:var(--muted);width:70px}
.person .photo{position:relative;border-radius:50%;margin:0 auto 6px;background:linear-gradient(135deg,#c9a98f,#6d5646)}
.person b{display:block;font-size:7px;color:var(--ink);text-transform:uppercase}
.arrow{position:absolute;top:290px;width:20px;height:20px}

.d-schedule{height:307px;background:linear-gradient(160deg,#6d3a2a,#b8683f 40%,#d48f5c 60%,#7a4630)}
.d-schedule h2{position:absolute;top:60px;width:100%;text-align:center;color:#fff;font-size:27px;font-weight:800;text-transform:uppercase}
.d-schedule p{position:absolute;left:250px;top:110px;width:394px;text-align:center;color:#fff;font-size:12px;line-height:16px}
.d-schedule .btn{position:absolute;left:398px;top:200px;font-size:10px;padding:7px 16px}

.d-features{height:204px;display:flex}
.feature{flex:1;color:#fff;padding:32px 30px 0}
.feature svg{display:block;margin-bottom:14px}
.feature h3{font-size:12px;font-weight:800;text-transform:uppercase;margin-bottom:7px}
.feature p{font-size:9px;line-height:13px}

.d-footer{height:281px;background:var(--night);color:#bbb}
.d-footer .brand{position:absolute;left:26px;top:80px;font-size:19px}
.d-footer .brand .mark{width:46px;height:46px}
.f-col{position:absolute;top:48px;font-size:8px;line-height:12px}
.f-col h4{color:#fff;font-size:8px;font-weight:700;text-transform:uppercase;margin-bottom:10px}
.f-row{display:flex;gap:8px;align-items:flex-start;margin-bottom:12px}
.f-row i{display:block;width:9px;height:9px;border-radius:50%;background:#888;flex:none;margin-top:2px}
.f-social .f-row i{width:14px;height:14px;background:#2b7fd0;margin-top:0}
.copy{position:absolute;left:0;right:0;bottom:0;height:36px;border-top:1px solid var(--night-line);font-size:7px;padding:14px 26px;color:#888}

/* ===== mobile ===== */
.mob{position:absolute;left:956px;top:33px;width:191px}
.mob section,.mob header,.mob footer{position:relative;width:100%;overflow:hidden}
.m-header{height:132px;background:var(--paper)}
.m-header .brand{position:absolute;left:8px;top:10px;font-size:11px}
.m-header .brand .mark{width:26px;height:26px}
.burger{position:absolute;right:8px;top:12px;width:24px;height:24px;background:var(--purple)}
.m-header .call{left:8px;top:56px;gap:6px}
.m-header .call .icon{width:18px;height:18px}
.m-header .call strong{font-size:12px}
.m-header .call small{font-size:6px}
.m-header .nav{left:8px;top:92px;width:175px}
.m-header .nav a{width:35px;height:18px;line-height:18px;font-size:5px}
.m-hero{height:273px;background:linear-gradient(130deg,#7b3d31,#b45c49 45%,#d79b82 70%,#8d4a3b)}
.m-hero h1{position:absolute;left:10px;top:45px;color:#fff;font-size:20px;line-height:22px;font-weight:800;text-transform:uppercase}
.m-hero .btn{position:absolute;left:10px;top:110px;font-size:7px;padding:5px 9px}
.m-hero .dots{left:75px;bottom:12px;gap:4px}
.m-hero .dots i{width:6px;height:6px}
.m-classes{height:1276px;background:var(--mist);padding-top:30px}
.m-classes h2{text-align:center;font-size:13px;font-weight:800;text-transform:uppercase;margin-bottom:10px}
.m-card{width:160px;height:290px;margin:0 auto 14px}
.m-card .photo{position:relative;height:150px}
.m-card .body{height:140px;padding:12px 10px;color:#fff}
.m-card h3{font-size:8px;font-weight:800;text-transform:uppercase;margin-bottom:6px}
.m-card p{font-size:7px;line-height:10px;margin-bottom:8px}
.m-card .btn{background:#fff;color:var(--ink);font-size:6px;padding:4px 7px}
.m-welcome{height:528px;background:var(--paper);padding:24px 8px}
.m-welcome h2{font-size:15px;line-height:18px;font-weight:800;color:var(--coral);text-transform:uppercase;margin-bottom:10px}
.m-welcome h2 span{display:block;color:var(--yellow)}
.m-welcome .photo{position:relative;height:170px;background:linear-gradient(135deg,#d8dde4,#8a9bb0 55%,#4a5a70);margin-bottom:12px}
.m-welcome p{font-size:7.5px;line-height:11px;color:var(--muted);margin-bottom:12px}
.m-welcome .btn{font-size:8px;padding:6px 12px}
.m-news{height:824px;background:var(--mist);padding:18px 8px}
.m-news h2{text-align:center;font-size:12px;font-weight:800;text-transform:uppercase;margin-bottom:12px}
.m-news-card{background:#fff;margin-bottom:12px;height:246px}
.m-news-card .photo{position:relative;height:110px;background:linear-gradient(135deg,#c9c2b6,#8b8578 60%,#5b564e)}
.m-news-card .body{padding:10px 8px}
.m-news-card h3{font-size:7px;line-height:10px;font-weight:800;text-transform:uppercase;margin-bottom:5px}
.m-news-card p{font-size:6.5px;line-height:9px;color:var(--muted);margin-bottom:7px}
.m-news-card .btn{font-size:6px;padding:3px 7px}
.m-testi{height:346px;background:var(--paper);padding:22px 12px;text-align:center}
.m-testi h2{font-size:12px;font-weight:800;text-transform:uppercase;margin-bottom:14px}
.m-testi p{font-size:8px;line-height:12px;margin-bottom:14px}
.m-testi .photo{position:relative;width:40px;height:40px;border-radius:50%;margin:0 auto 5px;background:linear-gradient(135deg,#c9a98f,#6d5646)}
.m-testi b{display:block;font-size:6px;text-transform:uppercase}
.m-testi small{display:block;font-size:5.5px;color:var(--muted)}
.m-schedule{height:346px;background:linear-gradient(160deg,#6d3a2a,#b8683f 45%,#d48f5c 65%,#7a4630);padding:60px 14px;text-align:center;color:#fff}
.m-schedule h2{font-size:15px;line-height:18px;font-weight:800;text-transform:uppercase;margin-bottom:10px}
.m-schedule p{font-size:8px;line-height:12px;margin-bottom:14px}
.m-schedule .btn{font-size:7px;padding:5px 10px}
.m-feature{height:181px;color:#fff;padding:22px 12px}
.m-feature svg{display:block;margin-bottom:10px}
.m-feature h3{font-size:9px;font-weight:800;text-transform:uppercase;margin-bottom:6px}
.m-feature p{font-size:7px;line-height:10px}
.m-footer{height:578px;background:var(--night);color:#bbb;padding:20px 12px;font-size:6.5px;line-height:10px}
.m-footer .brand{font-size:12px;margin-bottom:22px}
.m-footer .brand .mark{width:30px;height:30px}
.m-footer h4{color:#fff;font-size:7px;text-transform:uppercase;margin:14px 0 8px}
.m-footer .f-row{gap:6px;margin-bottom:8px}
.m-footer .f-row i{width:7px;height:7px}
.m-footer .f-social .f-row i{width:11px;height:11px}
.m-footer .copy{padding:12px;font-size:5.5px;height:30px}
</style>
</head>
<body>

<!-- ================= DESKTOP ================= -->
<div class="desk">
  <header class="d-header">
    <div class="brand"><span class="mark"></span>Stonepath<br>Academy</div>
    <div class="follow"><span>FOLLOW US</span><i></i><i></i><i></i></div>
    <div class="call">
      <span class="icon"><svg width="12" height="12" viewBox="0 0 24 24"><path d="M6.6 10.8a15 15 0 006.6 6.6l2.2-2.2a1 1 0 011-.25 11.4 11.4 0 003.6.6 1 1 0 011 1V20a1 1 0 01-1 1A17 17 0 013 4a1 1 0 011-1h3.5a1 1 0 011 1c0 1.25.2 2.45.6 3.6a1 1 0 01-.25 1z" fill="#fff"/></svg></span>
      <div><small>CALL US NOW</small><strong>555.014.2290</strong></div>
    </div>
    <nav class="nav"><a>Home</a><a>About us</a><a>Classes</a><a>Programs</a><a>Contact</a></nav>
  </header>

  <section class="d-hero" role="img" aria-label="Photo of a child's hands holding a fossil rock sample">
    <h1>Geology<br>Classes</h1>
    <span class="btn">Read more</span>
    <div class="dots"><i></i><i></i><i class="on"></i><i></i><i></i></div>
  </section>

  <section class="d-classes">
    <h2 class="sec-title">Geology Classes</h2>
    <article class="class-card" style="left:83px">
      <div class="photo" role="img" aria-label="Child studying a rock with a magnifying glass" style="background:linear-gradient(135deg,#8fbf6a,#4f7f3c)"></div>
      <div class="body bg-coral"><h3>Lorem ipsum is simp</h3><p>Sed ut perspiciatis unde omnis iste natus error sit voluptatem accusantium doloremque.</p><span class="btn">Read more</span></div>
    </article>
    <article class="class-card" style="left:267px">
      <div class="photo" role="img" aria-label="Layered rock formation" style="background:linear-gradient(135deg,#c28a55,#7a4a2c)"></div>
      <div class="body bg-teal"><h3>Lorem ipsum is simp</h3><p>Sed ut perspiciatis unde omnis iste natus error sit voluptatem accusantium doloremque.</p><span class="btn">Read more</span></div>
    </article>
    <article class="class-card" style="left:455px">
      <div class="photo" role="img" aria-label="Rock samples held in hands" style="background:linear-gradient(135deg,#b58b74,#6e4b3c)"></div>
      <div class="body bg-purple"><h3>Lorem ipsum is simp</h3><p>Sed ut perspiciatis unde omnis iste natus error sit voluptatem accusantium doloremque.</p><span class="btn">Read more</span></div>
    </article>
    <article class="class-card" style="left:643px">
      <div class="photo" role="img" aria-label="Collection of minerals on a table" style="background:linear-gradient(135deg,#a9a29a,#5e5852)"></div>
      <div class="body bg-coral"><h3>Lorem ipsum is simp</h3><p>Sed ut perspiciatis unde omnis iste natus error sit voluptatem accusantium doloremque.</p><span class="btn">Read more</span></div>
    </article>
  </section>

  <section class="d-welcome">
    <div class="welcome-text">
      <h2>Welcome to <span>Stonepath</span></h2>
      <p>But I must explain to you how all this mistaken idea of denouncing pleasure and praising pain was born and I will give you a complete account of the system, and expound the actual teachings of the great explorer of the truth, the master-builder of human happiness. No one rejects, dislikes, or avoids pleasure itself, because it is pleasure, but because those who do not know how to pursue pleasure rationally encounter consequences that are extremely painful.</p>
      <span class="btn">Read more</span>
    </div>
    <div class="photo" role="img" aria-label="Child learning at a desktop computer"></div>
  </section>

  <section class="d-news">
    <h2 class="sec-title">Latest News</h2>
    <article class="news-card" style="left:106px">
      <div class="photo" role="img" aria-label="Parent and child learning together at home"></div>
      <div class="body"><h3>At vero eos et accusamus et iusto odio dignissi</h3><p>But I must explain to you how all this mistaken idea of denouncing pleasure was born and I will give you a complete account.</p><span class="btn">Read more</span></div>
    </article>
    <article class="news-card" style="left:337px">
      <div class="photo" role="img" aria-label="Children working on a laptop"></div>
      <div class="body"><h3>At vero eos et accusamus et iusto odio dignissi</h3><p>But I must explain to you how all this mistaken idea of denouncing pleasure was born and I will give you a complete account.</p><span class="btn">Read more</span></div>
    </article>
    <article class="news-card" style="left:567px">
      <div class="photo" role="img" aria-label="Hands typing on a laptop keyboard"></div>
      <div class="body"><h3>At vero eos et accusamus et iusto odio dignissi</h3><p>But I must explain to you how all this mistaken idea of denouncing pleasure was born and I will give you a complete account.</p><span class="btn">Read more</span></div>
    </article>
  </section>

  <section class="d-testi">
    <h2 class="sec-title">Testimonials</h2>
    <span class="qmark" style="left:194px;top:110px">“</span>
    <p class="quote">On the other hand, we denounce with righteous indignation and dislike men who are so beguiled and demoralized by the charms of pleasure of the moment, so blinded by desire, that they cannot foresee the pain and trouble that are bound to ensue; and equal blame belongs to those who fail in their duty.</p>
    <span class="qmark" style="left:676px;top:186px">”</span>
    <svg class="arrow" style="left:270px" viewBox="0 0 20 20"><path d="M13 3L6 10l7 7" stroke="#999" stroke-width="2" fill="none"/></svg>
    <div class="people">
      <div class="person"><div class="photo" role="img" aria-label="Parent portrait" style="width:38px;height:38px;margin-top:14px"></div><b>Mara Ellis</b>Parent</div>
      <div class="person"><div class="photo" role="img" aria-label="Tutor portrait" style="width:62px;height:62px"></div><b>Theo Grant</b>Science Tutor</div>
      <div class="person"><div class="photo" role="img" aria-label="Parent portrait" style="width:38px;height:38px;margin-top:14px"></div><b>Rhea Novak</b>Homeschooler</div>
    </div>
    <svg class="arrow" style="left:604px" viewBox="0 0 20 20"><path d="M7 3l7 7-7 7" stroke="#999" stroke-width="2" fill="none"/></svg>
  </section>

  <section class="d-schedule" role="img" aria-label="Red rock canyon landscape">
    <h2>Class Schedule</h2>
    <p>On the other hand, we denounce with righteous indignation and dislike men who are so beguiled and demoralized by the charms of pleasure of the moment, which is the same as saying through shrinking from toil and pain. These cases are perfectly simple and easy to distinguish.</p>
    <span class="btn">Read more</span>
  </section>

  <section class="d-features">
    <div class="feature bg-coral">
      <svg width="34" height="30" viewBox="0 0 34 30" fill="none" stroke="#fff" stroke-width="2"><rect x="2" y="2" width="30" height="20" rx="1"/><path d="M12 28h10M17 22v6"/></svg>
      <h3>At vero eos et accusa</h3><p>On the other hand, we denounce with righteous indignation and dislike men who are so beguiled.</p>
    </div>
    <div class="feature bg-teal">
      <svg width="34" height="30" viewBox="0 0 34 30" fill="#fff"><circle cx="17" cy="8" r="5"/><path d="M8 26c0-6 4-9 9-9s9 3 9 9z"/><circle cx="6" cy="11" r="3.5"/><circle cx="28" cy="11" r="3.5"/><path d="M0 25c0-4 2.5-6 6-6s6 2 6 6zM22 25c0-4 2.5-6 6-6s6 2 6 6z"/></svg>
      <h3>At vero eos et accusa</h3><p>On the other hand, we denounce with righteous indignation and dislike men who are so beguiled.</p>
    </div>
    <div class="feature bg-purple">
      <svg width="30" height="30" viewBox="0 0 30 30" fill="none" stroke="#fff" stroke-width="2"><circle cx="15" cy="15" r="13"/><ellipse cx="15" cy="15" rx="6" ry="13"/><path d="M2 15h26M4 8h22M4 22h22"/></svg>
      <h3>At vero eos et accusa</h3><p>On the other hand, we denounce with righteous indignation and dislike men who are so beguiled.</p>
    </div>
  </section>

  <footer class="d-footer">
    <div class="brand"><span class="mark"></span>Stonepath<br>Academy</div>
    <div class="f-col" style="left:250px;width:170px">
      <h4>Contact us</h4>
      <div class="f-row"><i></i><span>14 Quarry Lane 2<br>4200 AK, Millbrook, The Valley</span></div>
      <div class="f-row"><i></i><span>555.014.2290</span></div>
      <div class="f-row"><i></i><span>hello@stonepath.example</span></div>
    </div>
    <div class="f-col" style="left:530px">
      <h4>Menu</h4>Home<br>About us<br>Classes<br>Programs<br>Blog<br>Contact
    </div>
    <div class="f-col f-social" style="left:660px">
      <h4>Connect with us</h4>
      <div class="f-row"><i></i><span>Social One</span></div>
      <div class="f-row"><i></i><span>Social Two</span></div>
      <div class="f-row"><i></i><span>Social Three</span></div>
    </div>
    <div class="copy">Copyright © 2019 All Rights Reserved</div>
  </footer>
</div>

<!-- ================= MOBILE ================= -->
<div class="mob">
  <header class="m-header">
    <div class="brand"><span class="mark"></span>Stonepath<br>Academy</div>
    <span class="burger"></span>
    <div class="call">
      <span class="icon"><svg width="9" height="9" viewBox="0 0 24 24"><path d="M6.6 10.8a15 15 0 006.6 6.6l2.2-2.2a1 1 0 011-.25 11.4 11.4 0 003.6.6 1 1 0 011 1V20a1 1 0 01-1 1A17 17 0 013 4a1 1 0 011-1h3.5a1 1 0 011 1c0 1.25.2 2.45.6 3.6a1 1 0 01-.25 1z" fill="#fff"/></svg></span>
      <div><small>CALL US NOW</small><strong>555.014.2290</strong></div>
    </div>
    <nav class="nav"><a>Home</a><a>About us</a><a>Classes</a><a>Programs</a><a>Contact</a></nav>
  </header>

  <section class="m-hero" role="img" aria-label="Photo of a child's hands holding a fossil rock sample">
    <h1>Geology<br>Classes</h1>
    <span class="btn">Read more</span>
    <div class="dots"><i></i><i></i><i class="on"></i><i></i></div>
  </section>

  <section class="m-classes">
    <h2>Geology Classes</h2>
    <article class="m-card"><div class="photo" role="img" aria-label="Child studying a rock with a magnifying glass" style="background:linear-gradient(135deg,#8fbf6a,#4f7f3c)"></div><div class="body bg-coral"><h3>Lorem ipsum is simp</h3><p>Sed ut perspiciatis unde omnis iste natus error sit voluptatem accusantium doloremque.</p><span class="btn">Read more</span></div></article>
    <article class="m-card"><div class="photo" role="img" aria-label="Layered rock formation" style="background:linear-gradient(135deg,#c28a55,#7a4a2c)"></div><div class="body bg-teal"><h3>Lorem ipsum is simp</h3><p>Sed ut perspiciatis unde omnis iste natus error sit voluptatem accusantium doloremque.</p><span class="btn">Read more</span></div></article>
    <article class="m-card"><div class="photo" role="img" aria-label="Rock samples held in hands" style="background:linear-gradient(135deg,#b58b74,#6e4b3c)"></div><div class="body bg-purple"><h3>Lorem ipsum is simp</h3><p>Sed ut perspiciatis unde omnis iste natus error sit voluptatem accusantium doloremque.</p><span class="btn">Read more</span></div></article>
    <article class="m-card"><div class="photo" role="img" aria-label="Collection of minerals on a table" style="background:linear-gradient(135deg,#a9a29a,#5e5852)"></div><div class="body bg-coral"><h3>Lorem ipsum is simp</h3><p>Sed ut perspiciatis unde omnis iste natus error sit voluptatem accusantium doloremque.</p><span class="btn">Read more</span></div></article>
  </section>

  <section class="m-welcome">
    <h2>Welcome to <span>Stonepath</span></h2>
    <div class="photo" role="img" aria-label="Child learning at a desktop computer"></div>
    <p>But I must explain to you how all this mistaken idea of denouncing pleasure and praising pain was born and I will give you a complete account of the system, and expound the actual teachings of the great explorer of the truth, the master-builder of human happiness. No one rejects, dislikes, or avoids pleasure itself, because it is pleasure, but because those who do not know how to pursue pleasure rationally encounter consequences that are extremely painful.</p>
    <span class="btn">Read more</span>
  </section>

  <section class="m-news">
    <h2>Latest News</h2>
    <article class="m-news-card"><div class="photo" role="img" aria-label="Parent and child learning together at home"></div><div class="body"><h3>At vero eos et accusamus et iusto odio dignissi</h3><p>But I must explain to you how all this mistaken idea of denouncing pleasure was born.</p><span class="btn">Read more</span></div></article>
    <article class="m-news-card"><div class="photo" role="img" aria-label="Children working on a laptop"></div><div class="body"><h3>At vero eos et accusamus et iusto odio dignissi</h3><p>But I must explain to you how all this mistaken idea of denouncing pleasure was born.</p><span class="btn">Read more</span></div></article>
    <article class="m-news-card"><div class="photo" role="img" aria-label="Hands typing on a laptop keyboard"></div><div class="body"><h3>At vero eos et accusamus et iusto odio dignissi</h3><p>But I must explain to you how all this mistaken idea of denouncing pleasure was born.</p><span class="btn">Read more</span></div></article>
  </section>

  <section class="m-testi">
    <h2>Testimonials</h2>
    <p>On the other hand, we denounce with righteous indignation and dislike men who are so beguiled and demoralized by the charms of pleasure of the moment, so blinded by desire, that they cannot foresee the pain and trouble.</p>
    <div class="photo" role="img" aria-label="Tutor portrait"></div>
    <b>Theo Grant</b>
    <small>Science Tutor</small>
  </section>

  <section class="m-schedule" role="img" aria-label="Red rock canyon landscape">
    <h2>Class<br>Schedule</h2>
    <p>On the other hand, we denounce with righteous indignation and dislike men who are so beguiled and demoralized by the charms of pleasure of the moment, which is the same as saying through shrinking from toil and pain.</p>
    <span class="btn">Read more</span>
  </section>

  <div class="m-feature bg-coral">
    <svg width="26" height="23" viewBox="0 0 34 30" fill="none" stroke="#fff" stroke-width="2"><rect x="2" y="2" width="30" height="20" rx="1"/><path d="M12 28h10M17 22v6"/></svg>
    <h3>At vero eos et accusa</h3><p>On the other hand, we denounce with righteous indignation and dislike men who are so beguiled.</p>
  </div>
  <div class="m-feature bg-teal">
    <svg width="26" height="23" viewBox="0 0 34 30" fill="#fff"><circle cx="17" cy="8" r="5"/><path d="M8 26c0-6 4-9 9-9s9 3 9 9z"/><circle cx="6" cy="11" r="3.5"/><circle cx="28" cy="11" r="3.5"/><path d="M0 25c0-4 2.5-6 6-6s6 2 6 6zM22 25c0-4 2.5-6 6-6s6 2 6 6z"/></svg>
    <h3>At vero eos et accusa</h3><p>On the other hand, we denounce with righteous indignation and dislike men who are so beguiled.</p>
  </div>
  <div class="m-feature bg-purple">
    <svg width="23" height="23" viewBox="0 0 30 30" fill="none" stroke="#fff" stroke-width="2"><circle cx="15" cy="15" r="13"/><ellipse cx="15" cy="15" rx="6" ry="13"/><path d="M2 15h26M4 8h22M4 22h22"/></svg>
    <h3>At vero eos et accusa</h3><p>On the other hand, we denounce with righteous indignation and dislike men who are so beguiled.</p>
  </div>

  <footer class="m-footer">
    <div class="brand"><span class="mark"></span>Stonepath<br>Academy</div>
    <h4>Contact us</h4>
    <div class="f-row"><i></i><span>14 Quarry Lane 2<br>4200 AK, Millbrook, The Valley</span></div>
    <div class="f-row"><i></i><span>555.014.2290</span></div>
    <div class="f-row"><i></i><span>hello@stonepath.example</span></div>
    <h4>Menu</h4>Home<br>About us<br>Classes<br>Programs<br>Blog<br>Contact
    <div class="f-social">
      <h4>Connect with us</h4>
      <div class="f-row"><i></i><span>Social One</span></div>
      <div class="f-row"><i></i><span>Social Two</span></div>
      <div class="f-row"><i></i><span>Social Three</span></div>
    </div>
    <div class="copy">Copyright © 2019 All Rights Reserved</div>
  </footer>
</div>

</body>
</html>
```